Velthorn Values Chart

I am the CEO of Velthorn http://velthorn-example.com

I want to create a Values Chart for our new company and I have attached a PDF of an example of such chart that I really like.

The objective of the values chart is to visually and creatively summarize how the company and its employees will build their unique company identity.

I have also attached a word document with the Velthorn logo and a visual that summarizes our business technology process. This visual can but does not have to be incorporated into the Values Chart. Below this visual are the statements that I have chosen to represent our values on the values chart.

Industry/Entity Type

Graphic Design

Requirements
Must have
• I would like the feel of this document to go along with the feel of our company website which I would describe as clean and crisp.

```html
<!DOCTYPE html>
<html lang="en">
<head>
<meta charset="utf-8">
<title>Velthorn Values Chart</title>
<link rel="stylesheet" href="https://fonts.googleapis.com/css2?family=Oswald:wght@500&display=swap">
<style>
  :root {
    --ink-bg: #1d1d1d;
    --ink-bg-light: #262626;
    --value-green: #8cc63e;
  }
  html, body {
    margin: 0;
    padding: 0;
    width: 851px;
    height: 1200px;
    overflow: hidden;
    background: var(--ink-bg);
  }
  .values-chart {
    display: block;
    width: 851px;
    height: 1200px;
    background: radial-gradient(ellipse at 50% 45%, var(--ink-bg-light) 0%, var(--ink-bg) 75%);
  }
  .value-word {
    fill: var(--value-green);
    font-family: "Oswald", "Arial Narrow", sans-serif;
    font-weight: 500;
    text-transform: uppercase;
  }
</style>
</head>
<body>
<svg class="values-chart" viewBox="0 0 593 836" width="851" height="1200" role="img" aria-label="Velthorn company values chart">
  <g class="value-cloud">
    <!-- outer columns -->
    <text class="value-word" transform="translate(143 230) rotate(-90)" font-size="39" textLength="215" lengthAdjust="spacingAndGlyphs">Raving Fans</text>
    <text class="value-word" transform="translate(143 805) rotate(-90)" font-size="39" textLength="558" lengthAdjust="spacingAndGlyphs">Passion for Cost and Production Efficiency</text>
    <text class="value-word" transform="translate(505 460) rotate(-90)" font-size="33" textLength="433" lengthAdjust="spacingAndGlyphs">Play to Win vs. Play to Participate</text>
    <text class="value-word" transform="translate(505 600) rotate(-90)" font-size="25" textLength="125" lengthAdjust="spacingAndGlyphs">Strength Based</text>
    <text class="value-word" transform="translate(505 800) rotate(-90)" font-size="17" textLength="65" lengthAdjust="spacingAndGlyphs">In Approach</text>

    <!-- upper block -->
    <text class="value-word" x="150" y="80" font-size="76" textLength="190" lengthAdjust="spacingAndGlyphs">Be Real</text>
    <text class="value-word" transform="translate(372 80) rotate(-90)" font-size="25" textLength="66" lengthAdjust="spacingAndGlyphs">Crisp</text>
    <text class="value-word" x="378" y="80" font-size="64" textLength="48" lengthAdjust="spacingAndGlyphs">W3</text>
    <text class="value-word" transform="translate(470 300) rotate(-90)" font-size="33" textLength="275" lengthAdjust="spacingAndGlyphs">Keep Things Simple</text>
    <text class="value-word" x="150" y="140" font-size="60" textLength="198" lengthAdjust="spacingAndGlyphs">Cash Flow</text>
    <text class="value-word" x="355" y="140" font-size="30" textLength="85" lengthAdjust="spacingAndGlyphs">Give Back</text>
    <text class="value-word" x="150" y="175" font-size="27" textLength="201" lengthAdjust="spacingAndGlyphs">Outstanding People</text>
    <text class="value-word" x="358" y="175" font-size="19" textLength="80" lengthAdjust="spacingAndGlyphs">Serve Others</text>

    <text class="value-word" x="150" y="232" font-size="52" textLength="152" lengthAdjust="spacingAndGlyphs">Speak the</text>
    <text class="value-word" x="150" y="300" font-size="71" textLength="150" lengthAdjust="spacingAndGlyphs">Truth</text>
    <text class="value-word" transform="translate(342 300) rotate(-90)" font-size="37" textLength="90" lengthAdjust="spacingAndGlyphs">Caring</text>
    <text class="value-word" transform="translate(382 300) rotate(-90)" font-size="39" textLength="109" lengthAdjust="spacingAndGlyphs">Courage</text>
    <text class="value-word" transform="translate(420 300) rotate(-90)" font-size="34" textLength="107" lengthAdjust="spacingAndGlyphs">Connect</text>

    <!-- middle block -->
    <text class="value-word" x="150" y="345" font-size="37" textLength="302" lengthAdjust="spacingAndGlyphs">Bulletproof Reliability</text>
    <text class="value-word" x="150" y="385" font-size="32" textLength="317" lengthAdjust="spacingAndGlyphs">Turning Problems into Profits</text>
    <text class="value-word" x="150" y="475" font-size="92" textLength="185" lengthAdjust="spacingAndGlyphs">Direct</text>
    <text class="value-word" x="345" y="425" font-size="27" textLength="120" lengthAdjust="spacingAndGlyphs">Value Added</text>
    <text class="value-word" x="345" y="453" font-size="28" textLength="120" lengthAdjust="spacingAndGlyphs">Marketing</text>
    <text class="value-word" x="345" y="475" font-size="17" textLength="120" lengthAdjust="spacingAndGlyphs">Irresistible Offers</text>
    <text class="value-word" x="150" y="520" font-size="39" textLength="188" lengthAdjust="spacingAndGlyphs">Communication</text>
    <text class="value-word" x="350" y="520" font-size="30" textLength="120" lengthAdjust="spacingAndGlyphs">Communicate</text>

    <!-- lower block -->
    <text class="value-word" x="150" y="545" font-size="18" textLength="70" lengthAdjust="spacingAndGlyphs">Relentless</text>
    <text class="value-word" x="150" y="605" font-size="62" textLength="167" lengthAdjust="spacingAndGlyphs">Passion</text>
    <text class="value-word" x="328" y="570" font-size="33" textLength="150" lengthAdjust="spacingAndGlyphs">Resourcefulness</text>
    <text class="value-word" x="328" y="598" font-size="16" textLength="150" lengthAdjust="spacingAndGlyphs">You Get What You Focus On</text>
    <text class="value-word" x="150" y="645" font-size="32" textLength="325" lengthAdjust="spacingAndGlyphs">Cleanest People in Waste</text>
    <text class="value-word" x="150" y="680" font-size="28" textLength="145" lengthAdjust="spacingAndGlyphs">Protecting the</text>
    <text class="value-word" x="305" y="690" font-size="49" textLength="200" lengthAdjust="spacingAndGlyphs">Environment</text>
    <text class="value-word" x="150" y="705" font-size="25" textLength="114" lengthAdjust="spacingAndGlyphs">Model After</text>
    <text class="value-word" x="150" y="730" font-size="25" textLength="114" lengthAdjust="spacingAndGlyphs">People Far</text>
    <text class="value-word" x="280" y="730" font-size="39" textLength="225" lengthAdjust="spacingAndGlyphs">Powerful Alliances</text>
    <text class="value-word" x="150" y="775" font-size="43" textLength="120" lengthAdjust="spacingAndGlyphs">Greater</text>
    <text class="value-word" x="150" y="805" font-size="30" textLength="120" lengthAdjust="spacingAndGlyphs">Persistent</text>
    <text class="value-word" x="285" y="805" font-size="84" textLength="200" lengthAdjust="spacingAndGlyphs">Flexible</text>
  </g>
</svg>
</body>
</html>
```